Redesign of Current Wix Website - Event Production Company

Our website is www.tqlgatherings.com and we need a redesign. We are full service event production company offering clients services including event management, graphics and content creation, vendor sourcing and management, contract review, audio visual production and venue selection. We would like our website to look more like an event management company, not just an audio visual company which it looks like now.
We want to look more like www.brivamedia.com
Our Wix account is FILLED with logos, pictures and all the graphics you will need and we can assist with assets, categories and text.
On the Logo, I want to move away from "TQL Gatherings" and move to "Halvorin Event Production" and I would like a redesigned logo with the same center element but a name change. I do have the art work files for the logo, vector and ai.

Target Market(s)

Event Planners and people that book event services. Assistants of CEOs. Marketing Directors. Gala Chairpersons and people in positions to purchase large scale event production

Industry/Entity Type

Event Management and Production - Corporate and Social

Coding

Coded - Design and coding required

Font styles to use
Other font styles liked:
• my logo is multicolor. look at it before you design

Colors
0054AA
0677BA
7BADD7
CADEEF
E8F1F8
6B429C
8869AF
B7A5CE
E3DAEB
F3F0F8

Requirements
Must have
• A clean professional look that shows the client who we are and what we do, and the full scope of what we do.
Nice to have
• www.brivamedia.com ; https://theroamingledger.com/ look at these two website We are going after venues, planners end clients. Much like the briva media page.

```html
<!DOCTYPE html>
<html lang="en">
<head>
<meta charset="utf-8">
<title>Halvorin Event Production</title>
<link href="https://fonts.googleapis.com/css2?family=Bebas+Neue&family=DM+Sans:wght@400;500;700&display=swap" rel="stylesheet">
<style>
:root{
  --blue:#0054AA;
  --blue-mid:#0677BA;
  --blue-light:#7BADD7;
  --purple:#6B429C;
  --ink:#1c1c1c;
  --black:#000;
  --white:#fff;
  --card-line:#d9d9d9;
}
*{margin:0;padding:0;box-sizing:border-box}
html,body{width:1200px;height:3820px;overflow:hidden}
body{font-family:"DM Sans",sans-serif;color:var(--ink);background:var(--white)}
section,header,footer{position:relative;width:1200px}
.abs{position:absolute}
.display{font-family:"Bebas Neue",sans-serif;font-weight:400;letter-spacing:.5px;line-height:1}

/* hero */
.hero{height:666px;background:
  radial-gradient(ellipse at 50% 30%,#3a7fd6 0%,#1b3f8f 35%,transparent 65%),
  linear-gradient(180deg,#3b2a7a 0%,#17307a 40%,#0a1330 75%,#000 100%);color:var(--white)}
.brand{display:flex;align-items:center;gap:8px;font-weight:700;font-size:15px;line-height:1;color:var(--white)}
.brand-dot{width:36px;height:36px;border-radius:50%;background:#2a2a3a;border:2px solid var(--white)}
.nav{left:64px;top:26px;right:60px;height:40px}
.nav-links{position:absolute;left:277px;top:10px;display:flex;gap:0;font-size:20px;font-weight:500}
.nav-links span{margin-right:47px}
.btn{display:inline-flex;align-items:center;justify-content:center;background:var(--white);color:var(--blue);font-weight:700;border-radius:4px}
.nav .btn{position:absolute;right:0;top:0;width:163px;height:42px;font-size:20px}
.hero-title{top:136px;width:100%;text-align:center;font-size:66px;line-height:73px}
.hero-sub{top:282px;width:100%;text-align:center;font-size:26px}

/* section heads */
.sec-head{display:flex;align-items:center;justify-content:center;gap:24px;width:100%}
.num{width:64px;height:64px;border-radius:50%;border:3px solid var(--blue);display:flex;align-items:center;justify-content:center;font-family:"Bebas Neue",sans-serif;font-size:46px;color:#111;line-height:1;padding-top:4px}
.sec-title{font-size:64px;color:var(--purple);padding-top:6px}

.what{height:868px}
.what .sec-head{top:739px;top:73px}
.intro{left:225px;width:750px;text-align:center;font-size:26px;line-height:39px;color:#222}
.intro b{font-weight:500}
.photo{top:569px;height:233px;background:linear-gradient(135deg,#5b6470,#2d333c)}

.services{height:925px;background:var(--blue)}
.services .num{border-color:var(--white);color:var(--white)}
.services .sec-title{color:var(--white)}
.grid{left:99px;top:151px;width:1000px;display:grid;grid-template-columns:repeat(3,1fr);row-gap:9px}
.tile{height:332px;padding:28px 34px;color:var(--white);font-size:46px;line-height:54px;background:linear-gradient(160deg,#8a8a8a,#3a3a3a)}

.why{height:675px}
.cards{left:108px;top:166px;width:984px;display:grid;grid-template-columns:479px 479px;gap:26px}
.card{height:207px;border:2px solid var(--card-line);border-radius:10px;box-shadow:0 3px 8px rgba(0,0,0,.12);display:flex;align-items:center;padding:0 50px}
.card svg{flex:0 0 82px;height:82px;margin-right:30px}
.card h3{font-size:27px;font-weight:500;margin-bottom:8px}
.card p{font-size:19px;line-height:26px;color:#333}

.connect{height:360px;background:var(--blue);color:var(--white)}
.eyebrow{left:108px;top:52px;font-size:21px}
.connect h2{left:108px;top:95px;font-size:66px}
.connect .sub{left:108px;top:170px;font-size:28px}
.connect .btn{left:108px;top:252px;width:163px;height:41px;font-size:20px}
.hall{left:647px;top:34px;width:444px;height:326px;background:linear-gradient(135deg,#dfe9f5,#7BADD7 55%,#2b2b3a)}

.gap{height:33px}
.foot{height:293px;background:var(--black);color:var(--white)}
.foot .brand{left:58px;top:55px;font-size:15px}
.social{right:58px;top:55px;display:flex;gap:10px}
.social span{width:38px;height:38px;border-radius:50%;border:2px solid var(--white)}
.foot-links{left:58px;font-size:20px;font-weight:500;display:flex;gap:42px}
.touch{right:46px;top:140px;font-size:36px;text-decoration:underline;text-underline-offset:4px}
.phone{right:46px;top:196px;font-size:36px}
</style>
</head>
<body>

<header class="hero">
  <div class="nav abs">
    <div class="brand"><span class="brand-dot"></span><span>Halvorin Event<br>Production</span></div>
    <nav class="nav-links"><span>What We Do</span><span>Services &#8964;</span><span>Work</span><span>Contact Us</span></nav>
    <a class="btn">Get a Quote</a>
  </div>
  <div class="hero-bg abs" role="img" aria-label="Concert crowd silhouetted under blue stage lights" style="inset:0;z-index:0"></div>
  <h1 class="hero-title abs display" style="z-index:1">Together, we create<br>powerful experiences</h1>
  <p class="hero-sub abs" style="z-index:1">We are ready to help with the production and managing your event</p>
</header>

<section class="what">
  <div class="sec-head abs"><span class="num">1</span><h2 class="sec-title display">What we do</h2></div>
  <p class="intro abs" style="top:163px"><b>Halvorin Event Production</b> is a full-service event production company that specializes in creating amazing experiences for our clients. We are dedicated to helping you bring your vision to life through our expert audio visual, planning, logistics, lighting, staging, and design services.</p>
  <p class="intro abs" style="top:399px">Our team of professionals strive to deliver a unique and unparalleled event experience to each of our clients. We also offer many production services to choose from.</p>
  <div class="photo abs" style="left:0;width:243px" role="img" aria-label="Live stream camera and control desk in a ballroom"></div>
  <div class="photo abs" style="left:268px;width:376px;background:linear-gradient(135deg,#e9eef4,#5d86b8 60%,#2c4f8a)" role="img" aria-label="Trade show booth with landscape graphics"></div>
  <div class="photo abs" style="left:669px;width:374px;background:linear-gradient(135deg,#4a4f57,#15181c)" role="img" aria-label="Audio mixing console and monitors"></div>
  <div class="photo abs" style="left:1068px;width:132px;background:linear-gradient(135deg,#6a4a5a,#1e1e26)" role="img" aria-label="Banquet hall with projection screen"></div>
</section>

<section class="services">
  <div class="sec-head abs" style="top:58px"><span class="num">2</span><h2 class="sec-title display">See our services</h2></div>
  <div class="grid abs">
    <div class="tile display" role="img" aria-label="Banquet event in a ballroom">Event<br>Management</div>
    <div class="tile display" style="background:linear-gradient(160deg,#b5b5b5,#3c3c3c)" role="img" aria-label="Crystal award trophies">Graphic<br>Creation</div>
    <div class="tile display" style="background:linear-gradient(160deg,#5e8fc4,#2a3f5e)" role="img" aria-label="Trade show booth">Vendor<br>Management</div>
    <div class="tile display" style="background:linear-gradient(160deg,#6a6a6a,#121212)" role="img" aria-label="Stage with camera on tripod">Contract<br>Review</div>
    <div class="tile display" style="background:linear-gradient(160deg,#9a9a9a,#444)" role="img" aria-label="Phone filming a live event">Audio Visual<br>Production</div>
    <div class="tile display" style="background:linear-gradient(160deg,#c4c4c4,#4a4a4a)" role="img" aria-label="Large venue set with dining tables">Venue<br>Selection</div>
  </div>
</section>

<section class="why">
  <div class="sec-head abs" style="top:75px"><span class="num">3</span><h2 class="sec-title display">Why choose us</h2></div>
  <div class="cards abs">
    <div class="card">
      <svg viewBox="0 0 82 82" aria-hidden="true"><rect x="4" y="12" width="74" height="66" rx="6" fill="none" stroke="#0054AA" stroke-width="6"/><rect x="4" y="12" width="74" height="16" fill="#0054AA"/><rect x="18" y="2" width="7" height="18" rx="3" fill="#0054AA"/><rect x="57" y="2" width="7" height="18" rx="3" fill="#0054AA"/><polygon points="41,36 46,48 59,48 49,56 53,69 41,61 29,69 33,56 23,48 36,48" fill="#0054AA"/></svg>
      <div><h3>Events</h3><p>Making your event vision a reality is what gets our team inspired.</p></div>
    </div>
    <div class="card">
      <svg viewBox="0 0 82 82" aria-hidden="true"><circle cx="41" cy="34" r="22" fill="#0054AA"/><rect x="30" y="58" width="22" height="8" rx="2" fill="#0054AA"/><rect x="33" y="69" width="16" height="7" rx="3" fill="#0054AA"/><g stroke="#0054AA" stroke-width="4" stroke-linecap="round"><line x1="41" y1="2" x2="41" y2="7"/><line x1="10" y1="34" x2="4" y2="34"/><line x1="72" y1="34" x2="78" y2="34"/><line x1="18" y1="11" x2="14" y2="7"/><line x1="64" y1="11" x2="68" y2="7"/></g></svg>
      <div><h3>Creative</h3><p>Our creative team is the reason why clients trust our team with their brands.</p></div>
    </div>
    <div class="card">
      <svg viewBox="0 0 82 82" aria-hidden="true"><path d="M12 44a29 29 0 0 1 58 0z" fill="#0054AA"/><rect x="6" y="44" width="70" height="8" rx="3" fill="#0054AA"/><rect x="35" y="8" width="12" height="22" fill="#fff"/><path d="M20 56h42a21 20 0 0 1-42 0z" fill="#0054AA"/></svg>
      <div><h3>Technology</h3><p>We use Technology because it helps us realize our your vision.</p></div>
    </div>
    <div class="card">
      <svg viewBox="0 0 82 82" aria-hidden="true"><rect x="2" y="18" width="78" height="56" rx="6" fill="#0054AA"/><rect x="26" y="10" width="30" height="12" rx="3" fill="#0054AA"/><circle cx="41" cy="46" r="17" fill="#fff"/><circle cx="41" cy="46" r="11" fill="#0054AA"/><circle cx="41" cy="46" r="5" fill="#fff"/></svg>
      <div><h3>Broadcast</h3><p>we push the boundaries of our virtual production to get the best results.</p></div>
    </div>
  </div>
</section>

<section class="connect">
  <p class="eyebrow abs">Halvorin Event Production</p>
  <h2 class="display abs">Let’s connect</h2>
  <p class="sub abs">Before Your Next Event</p>
  <a class="btn abs">Get a Quote</a>
  <div class="hall abs" role="img" aria-label="Isometric drawing of a conference hall with seats and stage screen"></div>
</section>

<div class="gap"></div>

<footer class="foot">
  <div class="brand abs"><span class="brand-dot"></span><span>Halvorin Event<br>Production</span></div>
  <div class="social abs" aria-label="Social profiles"><span></span><span></span><span></span></div>
  <nav class="foot-links abs" style="top:148px"><span>Home</span><span>What We Do</span><span>Services</span><span>Work</span></nav>
  <nav class="foot-links abs" style="top:207px"><span>Privacy Policy</span><span>Terms of Use</span><span>Contact Us</span></nav>
  <p class="touch abs display">Get In Touch</p>
  <p class="phone abs display">(888) 555-0142</p>
</footer>

</body>
</html>
```